Reed & Vale NC grand opening (for BILLBOARD)

Advertising the grand opening of our cannabis/hemp shop in NC. We will sell all things hemp (flower, cartridges, disposables, edibles, creams, lotions, pet products etc...)

Requirements
Must have
• include, open starting Aug 1, but grand opening Aug 15th.
Nice to have
• Difference slogan ideas "Save some cash, buy our grass" "Find your perfect high at Reed & Vale cannabis store" "Experience Nature's Gift: Reed & Vale Cannabis Store"

```html
<!DOCTYPE html>
<html lang="en">
<head>
<meta charset="utf-8">
<title>Reed &amp; Vale Grand Opening</title>
<link rel="stylesheet" href="https://fonts.googleapis.com/css2?family=Poppins:wght@400;500;700;800&display=swap">
<style>
:root{
  --page:#e9eaec;
  --forest-deep:#0f2a1c;
  --forest:#1f5a3a;
  --leaf:#2f8a4f;
  --lime:#7cc243;
  --navy:#1a1d4a;
  --band:#e6e7e9;
  --white:#ffffff;
  --bottle:#6a3a1e;
}
*{margin:0;padding:0;box-sizing:border-box}
html,body{width:1200px;height:2824px;overflow:hidden;background:var(--page);font-family:"Poppins",sans-serif;color:var(--navy)}
.flyer{position:absolute;left:85px;top:746px;width:1030px;height:1332px;background:var(--white);overflow:hidden;box-shadow:0 6px 18px rgba(0,0,0,.18)}
.hero{position:absolute;left:0;top:0;width:1030px;height:720px}
.brand{position:absolute;left:58px;top:90px;font-family:"Poppins",sans-serif;font-weight:500;font-size:78px;letter-spacing:-1px;color:var(--lime);line-height:1}
.product-art{position:absolute;left:90px;top:220px;width:345px;height:340px;border-radius:40% 40% 30% 30%;background:radial-gradient(ellipse at 50% 55%,#8a5230 0%,#5a3a1e 35%,#3c6b2c 70%,rgba(31,90,58,0) 100%)}
.headline{position:absolute;left:0;width:100%;text-align:center;top:580px;font-weight:800;font-size:60px;letter-spacing:-.5px;line-height:1}
.store{position:absolute;left:0;width:100%;text-align:center;top:645px;font-weight:700;font-size:50px;color:var(--lime);line-height:1}
.opening{position:absolute;left:0;width:100%;text-align:center;top:728px;white-space:nowrap;line-height:1}
.opening .small{font-size:32px;font-weight:500}
.opening .date{font-size:48px;font-weight:700}
.opening .grand{font-size:56px;font-weight:700;color:var(--lime)}
.detail-band{position:absolute;left:0;top:892px;width:1030px;height:338px;background:linear-gradient(#e4e5e7,#f5f5f6 60%,#e8e9eb)}
.event-date{position:absolute;left:277px;top:815px;width:370px;height:84px;background:var(--navy);color:var(--white);font-weight:800;font-size:72px;text-align:center;line-height:84px;letter-spacing:-1px;box-shadow:0 6px 10px rgba(0,0,0,.25)}
.event-date sup{font-size:40px;vertical-align:28px}
.promise{position:absolute;left:0;width:100%;text-align:center;top:912px;font-size:40px;font-weight:700;line-height:1}
.promise em{font-style:normal;color:var(--lime)}
.product-item{position:absolute;width:200px;margin-left:-100px;text-align:center;font-size:26px;font-weight:500}
.product-item svg{display:block;margin:0 auto 6px;width:60px;height:60px;stroke:var(--lime);fill:none;stroke-width:2.4;stroke-linecap:round;stroke-linejoin:round}
.contact-bar{position:absolute;left:0;top:1240px;width:1030px;height:92px;background:var(--lime);text-align:center}
.contact-bar .phone{display:block;font-size:30px;font-weight:700;color:var(--navy);padding-top:12px;line-height:1.2}
.contact-bar .address{display:block;font-size:20px;color:var(--white);line-height:1.4}
</style>
</head>
<body>
<main class="flyer">
  <svg class="hero" viewBox="0 0 1030 720" width="1030" height="720">
    <defs>
      <linearGradient id="foliage" x1="0" y1="0" x2="1" y2="1">
        <stop offset="0" stop-color="#14392a"/>
        <stop offset=".55" stop-color="#22603c"/>
        <stop offset="1" stop-color="#0f2a1c"/>
      </linearGradient>
      <linearGradient id="swoosh" x1="0" y1="0" x2="1" y2="0">
        <stop offset="0" stop-color="#2f8a4f"/>
        <stop offset="1" stop-color="#7cc243"/>
      </linearGradient>
    </defs>
    <rect width="1030" height="720" fill="url(#foliage)" role="img" aria-label="Photo of cannabis leaves on a dark green background"/>
    <path d="M0 520 C200 320 420 300 560 390 C700 480 860 470 1030 330 L1030 720 L0 720Z" fill="url(#swoosh)"/>
    <path d="M0 600 C230 380 440 380 600 450 C760 520 900 520 1030 450 L1030 720 L0 720Z" fill="#d4d6d9"/>
    <path d="M0 620 C240 400 450 410 620 480 C780 545 910 560 1030 510 L1030 720 L0 720Z" fill="var(--white)"/>
  </svg>

  <div class="brand">Reed &amp; Vale</div>
  <div class="product-art" role="img" aria-label="Illustration of a CBD oil dropper bottle framed by hemp leaves"></div>

  <h1 class="headline">EXPERIENCE NATURE'S GIFT:</h1>
  <h2 class="store">Reed &amp; Vale Cannabis Store</h2>
  <p class="opening"><span class="small">Open starting </span><span class="date">Aug 1,</span><span class="small"> but </span><span class="grand">GRAND OPENING</span></p>

  <section class="detail-band"></section>
  <div class="event-date">AUG 15<sup>TH</sup></div>
  <p class="promise">We will <em>SELL</em> all things <em>HEMP</em></p>

  <div class="product-item" style="left:90px;top:998px">
    <svg viewBox="0 0 60 60"><path d="M30 52V20M30 20C26 30 27 40 30 48C33 40 34 30 30 20M30 40C20 36 12 28 8 20C18 22 26 30 30 40M30 40C40 36 48 28 52 20C42 22 34 30 30 40M30 46C22 46 14 42 8 38M30 46C38 46 46 42 52 38"/></svg>Flower</div>
  <div class="product-item" style="left:315px;top:998px">
    <svg viewBox="0 0 60 60"><rect x="24" y="6" width="12" height="20" rx="2"/><rect x="22" y="26" width="16" height="14"/><path d="M26 40v12h8V40M14 33h4M42 33h4"/></svg>Cartridges</div>
  <div class="product-item" style="left:588px;top:998px">
    <svg viewBox="0 0 60 60"><rect x="22" y="4" width="16" height="52" rx="6"/><path d="M22 16h16M30 30v6"/></svg>Disposables</div>
  <div class="product-item" style="left:832px;top:998px">
    <svg viewBox="0 0 60 60"><rect x="20" y="4" width="20" height="8"/><rect x="14" y="12" width="32" height="42" rx="4"/><circle cx="30" cy="33" r="9"/></svg>Edibles</div>
  <div class="product-item" style="left:196px;top:1110px">
    <svg viewBox="0 0 60 60"><path d="M16 20c0-10 28-10 28 0"/><rect x="12" y="20" width="36" height="32" rx="4"/><path d="M30 28v16M22 36h16"/></svg>Creams</div>
  <div class="product-item" style="left:446px;top:1110px">
    <svg viewBox="0 0 60 60"><rect x="18" y="4" width="14" height="8"/><rect x="14" y="12" width="22" height="16" rx="2"/><path d="M20 28v24h10V28M44 30l6 10-6 10-6-10z"/></svg>Lotions</div>
  <div class="product-item" style="left:714px;top:1110px">
    <svg viewBox="0 0 60 60"><rect x="6" y="34" width="16" height="18"/><rect x="24" y="26" width="14" height="26"/><rect x="40" y="30" width="14" height="22"/><path d="M26 12l4 4 4-4a3 3 0 0 0-4-4 3 3 0 0 0-4 4z"/></svg>Pet Products</div>

  <footer class="contact-bar">
    <span class="phone">Ph: +1 555-204-7716</span>
    <span class="address">418 Maple Row #3, Cedar Falls, NY 12950, United States</span>
  </footer>
</main>
</body>
</html>
```